Homepage Redesign - Hi-tech business Law Firm

I'm looking for an updated graphic design (pdf file) for the homepage of dorvantlegal.ca (and which will form the general template of the other pages - but you don't need to design that). Detailed specs are in the Word file.

Deliverable is 1 pdf file that I find good looking, that sets forth the layout of the new page.

Target Market(s)

Sophisticated customers

Industry/Entity Type

Legal

Number of Pages Required

1 page

Requirements
Nice to have
• For a main background, tech type images to do with high powered boardrooms, computers, graphs, numbers, high tech manufacturing lines etc. Also, I tend to like blues and light greys, and uploaded a file today that shows my generally preferred layout, which a few of you have been getting close to.
Should not have
• Any mention of 'Personal Injury,' backgrounds that include books, or buildings with roman columns. Page should not be in dark colors or harsh on the eyes.

```html
<!DOCTYPE html>
<html lang="en">
<head>
<meta charset="utf-8">
<title>Dorvant Legal — Business Litigation Lawyers</title>
<link href="https://fonts.googleapis.com/css2?family=Rubik:wght@300;400;500;700&display=swap" rel="stylesheet">
<style>
:root{
  --navy:#0f3a5a;
  --blue:#1b5a8c;
  --link:#1f6aa5;
  --ink:#222;
  --text:#555;
  --muted:#888;
  --light:#f1f1f1;
  --line:#d8d8d8;
  --dark:#1e1f21;
  --star:#f5b301;
  --badge:#e4e7ea;
}
*{box-sizing:border-box;margin:0;padding:0}
html,body{width:1200px;height:4009px;overflow:hidden}
body{font-family:'Rubik',sans-serif;color:var(--ink);background:#fff;position:relative}
.wrap{width:960px;margin:0 auto;position:relative}
section,header,footer{position:relative;width:1200px}

.topbar{height:93px}
.topbar .wrap{display:flex;align-items:center;justify-content:space-between;height:93px}
.brand{display:flex;align-items:center;gap:10px}
.brand-mark{width:48px;height:48px;border:2px solid var(--navy);display:block}
.brand-name{font-family:'Rubik',sans-serif;font-weight:400;color:var(--navy);font-size:17px;letter-spacing:3px;line-height:1.1;text-transform:uppercase}
.contacts{display:flex;gap:28px;font-size:11px;color:var(--text)}
.contact{display:flex;align-items:center;gap:9px}
.contact .ico{width:26px;height:26px;background:var(--navy);display:flex;align-items:center;justify-content:center}
.contact a{color:var(--link);text-decoration:none}
.navbar{height:47px;background:var(--navy)}
.navbar .wrap{display:flex;align-items:center;justify-content:space-between;height:47px}
.nav{display:flex;gap:40px;list-style:none;color:#fff;font-size:12px;font-weight:500}
.nav li{display:flex;align-items:center;gap:6px}
.search{width:266px;height:28px;background:#fff;border:1px solid #ccc;display:flex;align-items:center;gap:8px;padding:0 12px;font-size:11px;color:#999}

.hero{height:498px;overflow:hidden}
.hero-art{position:absolute;right:0;top:0;width:600px;height:498px;background:linear-gradient(120deg,#fbfbfb 0%,#eef1f4 45%,#dfe3e7 100%)}
.hero-person{position:absolute;left:640px;top:20px;width:320px;height:478px;background:linear-gradient(180deg,#b8a898 0%,#3a3f48 35%,#1f232a 100%);border-radius:140px 140px 0 0}
.hero-copy{position:absolute;left:120px;top:140px}
.hero h1{font-size:46px;font-weight:700;color:#1a1a1a}
.hero .lead{font-size:29px;font-weight:300;color:#1a1a1a;line-height:36px;margin-top:16px}
.btns{display:flex;gap:10px;margin-top:34px}
.btn{height:34px;padding:0 16px;display:flex;align-items:center;gap:8px;font-size:11px;font-weight:500}
.btn-solid{background:var(--navy);color:#fff}
.btn-line{border:1px solid var(--line);color:var(--blue)}

.practice{height:461px;background:var(--light)}
.titled{display:flex;align-items:center;justify-content:center;gap:22px;font-size:30px;font-weight:400;color:#1a1a1a}
.titled::before,.titled::after{content:"";width:160px;height:1px;background:var(--navy)}
.practice .titled{padding-top:70px}
.cards{display:flex;gap:21px;margin-top:40px}
.card{width:306px;height:248px;background:#fff;padding:34px 26px}
.card h3{font-size:19px;font-weight:400;color:var(--blue);margin:20px 0 16px}
.card p{font-size:12px;line-height:20px;color:var(--text)}

.results{height:608px}
.results .wrap{display:flex;justify-content:space-between;padding-top:68px}
.intro{width:443px}
.eyebrow{font-size:12px;font-weight:500;color:var(--blue)}
.intro h2{font-size:29px;font-weight:400;margin:4px 0 20px}
.intro hr{border:0;height:2px;background:var(--navy);width:430px;margin-bottom:44px}
.intro p{font-size:12px;line-height:20px;color:var(--text);margin-bottom:18px}
.form{width:447px;height:473px;background:var(--light);padding:26px 27px}
.form h3{font-size:19px;font-weight:400;color:var(--blue)}
.form .sub{font-size:10px;color:var(--text);margin:6px 0 26px}
.lbl{font-size:11px;font-weight:500;margin-bottom:10px}
.lbl span{color:#d11}
.row{display:flex;gap:11px;margin-bottom:30px}
.field{flex:1;height:32px;background:#fff;border:1px solid #ddd;font-size:10px;color:#bbb;padding:10px}
.field.area{height:133px;margin-bottom:22px}
.formfoot{display:flex;justify-content:space-between;align-items:center;font-size:10px;color:var(--text);line-height:16px}
.formfoot b{color:var(--blue);font-weight:500}
.send{background:var(--navy);color:#fff;font-size:11px;font-weight:500;padding:10px 16px}

.badges{height:340px;background:var(--light)}
.arrow{position:absolute;top:96px;width:38px;height:38px;border-radius:50%;background:#fff;display:flex;align-items:center;justify-content:center}
.badge-row{position:absolute;left:227px;top:67px;display:flex;gap:67px}
.badge{width:339px}
.badge-box{height:106px;background:#fff;display:flex;align-items:center;justify-content:center}
.badge-shape{width:220px;height:50px;background:var(--badge);display:block}
.badge p{font-size:12px;line-height:20px;color:var(--text);text-align:center;margin-top:18px}

.block-head{display:flex;justify-content:space-between;align-items:center}
.block-head h2{font-size:29px;font-weight:400}
.viewall{border:1px solid var(--line);font-size:11px;font-weight:500;color:var(--blue);padding:10px 16px}
.news{height:404px}
.news .block-head{padding-top:66px}
.cols{display:flex;gap:66px;margin-top:38px}
.item{width:276px;display:flex;gap:20px}
.item svg{flex:none}
.item h4{font-size:12px;font-weight:500;line-height:20px;color:#222;margin-bottom:8px}
.item p{font-size:12px;line-height:20px;color:var(--text)}
.item .more{display:block;margin-top:40px;font-size:12px;font-weight:500;color:var(--blue)}
.news .wrap::after{content:"";position:absolute;left:0;right:0;top:400px;height:1px;background:#e6e6e6}
.wins{height:342px}
.wins .block-head{padding-top:52px}
.wins p b{color:var(--blue);font-weight:500}
.wins p strong{font-weight:500;color:#222}

.stats{height:397px;overflow:hidden;border-bottom:5px solid var(--navy)}
.stats-bg{position:absolute;inset:0;background:linear-gradient(90deg,#f0f0f0 0%,#fafafa 30%,#fafafa 70%,#eeeeee 100%)}
.stats-person{position:absolute;left:436px;top:23px;width:326px;height:374px;background:linear-gradient(180deg,#c6a992 0%,#8a7565 28%,#1d2026 48%,#15171b 100%);border-radius:150px 150px 0 0}
.stat{position:absolute;width:201px;height:100px;background:#fff;border:2px solid var(--navy);text-align:center;padding-top:14px}
.stat b{display:block;font-size:44px;font-weight:400;color:var(--navy);line-height:48px}
.stat span{font-size:12px;color:var(--text)}
.links{position:absolute;inset:0}

.reviews{height:498px}
.reviews .titled{padding-top:70px}
.review{margin-top:38px;height:280px;background:var(--light);padding:28px 27px}
.who{display:flex;align-items:center;gap:22px}
.avatar{width:67px;height:67px;background:linear-gradient(135deg,#d9c4b0,#7b6a5c)}
.who h4{font-size:19px;font-weight:400}
.who small{font-size:11px;color:var(--text)}
.stars{margin-left:auto;display:flex;gap:12px}
.review p{font-size:12px;line-height:20px;color:var(--text);margin-top:28px}
.dots{display:flex;gap:16px;justify-content:center;margin-top:26px}
.dots i{width:13px;height:13px;border-radius:50%;background:#dcdcdc}
.dots i:first-child{background:var(--navy)}

.footer{height:249px;background:var(--dark);color:#ccc}
.footer .wrap{display:flex;gap:70px;padding-top:52px}
.fleft{width:245px}
.fleft .brand-mark{border-color:#fff;background:#fff}
.fleft .brand-name{color:#9aa3ab}
.flist{list-style:none;margin-top:24px;font-size:11px}
.flist li{display:flex;align-items:center;gap:14px;margin-bottom:12px}
.flist .ico{width:24px;height:24px;background:var(--navy);display:flex;align-items:center;justify-content:center}
.flist a{color:var(--link)}
.fright{width:645px;font-size:10px;line-height:16px}
.offices{display:flex;gap:62px;margin-top:22px}
.offices h5{font-size:10px;font-weight:500;color:#fff;margin-bottom:8px}
.bottom{height:72px;background:var(--dark);border-top:1px solid #333}
.bottom .wrap{display:flex;justify-content:space-between;align-items:center;height:72px;font-size:10px;color:#aaa}
.bottom a{color:var(--link);margin-left:18px}
.share{display:flex;align-items:center;gap:18px}
.share i{width:16px;height:16px;border-radius:50%;background:#fff;display:block}
a{text-decoration:none}
</style>
</head>
<body>

<header class="topbar">
  <div class="wrap">
    <div class="brand">
      <span class="brand-mark"></span>
      <div class="brand-name">Dorvant<br>Legal</div>
    </div>
    <div class="contacts">
      <div class="contact"><span class="ico"><svg width="12" height="12" viewBox="0 0 12 12"><path d="M6 1a3.5 3.5 0 0 0-3.5 3.5C2.5 7.5 6 11 6 11s3.5-3.5 3.5-6.5A3.5 3.5 0 0 0 6 1z" fill="none" stroke="#fff"/><circle cx="6" cy="4.5" r="1.2" fill="#fff"/></svg></span>GTA - Hamilton - Niagara</div>
      <div class="contact"><span class="ico"><svg width="12" height="12" viewBox="0 0 12 12"><path d="M2 1.5h2.5l1 2.5-1.5 1a7 7 0 0 0 3 3l1-1.5 2.5 1V10a1 1 0 0 1-1 1A9 9 0 0 1 1 2.5a1 1 0 0 1 1-1z" fill="none" stroke="#fff"/></svg></span><a>555.214.7730</a></div>
      <div class="contact"><span class="ico"><svg width="12" height="10" viewBox="0 0 12 10"><rect x=".5" y=".5" width="11" height="9" fill="none" stroke="#fff"/><path d="M.5 .5 6 5l5.5-4.5" fill="none" stroke="#fff"/></svg></span><a>info@dorvantlegal.ca</a></div>
    </div>
  </div>
</header>
<nav class="navbar">
  <div class="wrap">
    <ul class="nav">
      <li>Practice Areas <svg width="8" height="5" viewBox="0 0 8 5"><path d="M1 1l3 3 3-3" fill="none" stroke="#fff" stroke-width="1.2"/></svg></li>
      <li>About <svg width="8" height="5" viewBox="0 0 8 5"><path d="M1 1l3 3 3-3" fill="none" stroke="#fff" stroke-width="1.2"/></svg></li>
      <li>News</li><li>Resources</li><li>Contact</li>
    </ul>
    <div class="search"><svg width="11" height="11" viewBox="0 0 11 11"><circle cx="4.5" cy="4.5" r="3.5" fill="none" stroke="#999"/><path d="M7 7l3 3" stroke="#999"/></svg>Search</div>
  </div>
</nav>

<section class="hero">
  <div class="hero-art" role="img" aria-label="Light technology backdrop with coloured hexagon outlines"></div>
  <div class="hero-person" role="img" aria-label="Portrait of lead lawyer in a dark suit"></div>
  <div class="hero-copy">
    <h1>Winning.</h1>
    <p class="lead">My clients depend on me for it.<br>Shouldn't you?</p>
    <div class="btns">
      <span class="btn btn-solid"><svg width="12" height="10" viewBox="0 0 12 10"><path d="M1 1h4l1 1 1-1h4v8H7L6 9.5 5 9H1z" fill="none" stroke="#fff"/></svg>Read More</span>
      <span class="btn btn-line"><svg width="12" height="10" viewBox="0 0 12 10"><rect x=".5" y="1.5" width="8" height="7" fill="none" stroke="#1b5a8c"/><path d="M8.5 4 11.5 2v6L8.5 6" fill="none" stroke="#1b5a8c"/></svg>Video Library</span>
    </div>
  </div>
</section>

<section class="practice">
  <div class="wrap">
    <h2 class="titled">Practice Areas</h2>
    <div class="cards">
      <div class="card">
        <svg width="54" height="52" viewBox="0 0 54 52" fill="none" stroke="#0f3a5a" stroke-width="1.4"><rect x="2" y="2" width="24" height="48"/><rect x="26" y="18" width="24" height="32"/><path d="M8 10h4M16 10h4M8 18h4M16 18h4M8 26h4M16 26h4M8 34h4M16 34h4M32 26h4M40 26h4M32 34h4M40 34h4M11 50v-8h6v8"/></svg>
        <h3>Business Litigation</h3>
        <p>Business disputes can have a serious impact upon your company's bottom line.</p>
      </div>
      <div class="card">
        <svg width="54" height="52" viewBox="0 0 54 52" fill="none" stroke="#0f3a5a" stroke-width="1.4"><path d="M16 2h22l12 12v36H16z"/><path d="M38 2v12h12"/><rect x="2" y="24" width="30" height="22"/><path d="M12 24v-4h10v4M2 33h30M14 31v5h6v-5"/></svg>
        <h3>Professional Negligence</h3>
        <p>When a professional has let you down, the impact can be devastating. I have the experience need to help.</p>
      </div>
      <div class="card">
        <svg width="54" height="52" viewBox="0 0 54 52" fill="none" stroke="#0f3a5a" stroke-width="1.4"><path d="M12 18a14 14 0 0 1 28 0 5 5 0 0 0-9 0 5 5 0 0 0-10 0 5 5 0 0 0-9 0zM26 18v12"/><path d="M2 36h8l10 2h10a3 3 0 0 1 0 6H18M30 42l14-6a3 3 0 0 1 3 5L30 50H10l-8-4"/></svg>
        <h3>Insurance</h3>
        <p>When your insurance company refuses to pay, you need a lawyer who has experience suing insurance companies, and winning</p>
      </div>
    </div>
  </div>
</section>

<section class="results">
  <div class="wrap">
    <div class="intro">
      <div class="eyebrow">Your Experienced Toronto and Hamilton Lawyers</div>
      <h2>Getting the Results That Matter</h2>
      <hr>
      <p>Dorvant Legal is a boutique litigation firm with law offices in Toronto and Hamilton. We concentrate our legal practice on complex business litigation, professional negligence (malpractice) claims, and insurance coverage disputes.</p>
      <p>We take an innovative approach to our client's legal problems, and are guided by the philosophy that our job is to get results.</p>
      <p>The lawyers at Dorvant Legal have the reputation for vigorously representing their clients' interests and competing hard to obtain the best possible results. With experience at all stages of legal disputes, the lawyers at Dorvant Legal are equally at home negotiating in a boardroom or presenting a case at trial.</p>
      <p>We hope that you take the time to explore our website to find out how our record of excellence, expertise and many years of experience can assist you.</p>
    </div>
    <div class="form">
      <h3>Case Evaluation</h3>
      <div class="sub">Fill out this form to schedule your initial consult with our lawyers.</div>
      <div class="lbl">Name <span>*</span></div>
      <div class="row"><div class="field">First Name</div><div class="field">Last Name</div></div>
      <div class="row" style="margin-bottom:10px"><div class="lbl" style="flex:1;margin-bottom:0">Email <span>*</span></div><div class="lbl" style="flex:1;margin-bottom:0">Phone <span>*</span></div></div>
      <div class="row"><div class="field">Email Address</div><div class="field">Phone Number</div></div>
      <div class="lbl">Case Details <span>*</span></div>
      <div class="field area">Case Details</div>
      <div class="formfoot">
        <div><span style="color:#d11">*</span> &nbsp;By using this site and/or submitting this form, I agree<br>&nbsp;&nbsp;&nbsp;to the <b>Privacy Policy</b> and <b>Terms of Use</b>.</div>
        <span class="send">Send</span>
      </div>
    </div>
  </div>
</section>

<section class="badges">
  <span class="arrow" style="left:119px"><svg width="14" height="12" viewBox="0 0 14 12"><path d="M13 6H1M6 1 1 6l5 5" fill="none" stroke="#1b5a8c" stroke-width="1.4"/></svg></span>
  <div class="badge-row">
    <div class="badge">
      <div class="badge-box"><span class="badge-shape" role="img" aria-label="Peer rating award badge"></span></div>
      <p>An excellent rating for a lawyer with some experience. This rating indicates the attorney is widely respected by their peers for high professional achievement and ethical standards.</p>
    </div>
    <div class="badge">
      <div class="badge-box"><span class="badge-shape" role="img" aria-label="Professional regulator membership badge"></span></div>
      <p>An excellent rating for a lawyer with some experience. This rating indicates the attorney is widely respected by their peers for high professional achievement and ethical standards.</p>
    </div>
  </div>
  <span class="arrow" style="left:1041px"><svg width="14" height="12" viewBox="0 0 14 12"><path d="M1 6h12M8 1l5 5-5 5" fill="none" stroke="#1b5a8c" stroke-width="1.4"/></svg></span>
</section>

<section class="news">
  <div class="wrap">
    <div class="block-head"><h2>Latest News</h2><span class="viewall">View All</span></div>
    <div class="cols">
      <div class="item">
        <svg width="27" height="27" viewBox="0 0 27 27" fill="none" stroke="#777"><rect x="1" y="5" width="21" height="21"/><path d="M5 1h21v21M5 11h8M5 15h13M5 19h13M15 10h4v3h-4z"/></svg>
        <div><h4>Dorvant Legal joins Global Referral Network</h4><p>Dorvant Legal, is now a member of Meridian Global Referral Network – the largest legal referral network in the world – comprising 283 member firms located in more than 160 countries.</p><span class="more">Read More</span></div>
      </div>
      <div class="item">
        <svg width="27" height="27" viewBox="0 0 27 27" fill="none" stroke="#777"><rect x="1" y="5" width="21" height="21"/><path d="M5 1h21v21M5 11h8M5 15h13M5 19h13M15 10h4v3h-4z"/></svg>
        <div><h4>How to Get the Most out of an Initial Consultation with a Lawyer</h4><p>If you're contemplating legal action, have been sued, are unsure of your legal standing in a particular situation, or need advice on an issue that has potential legal ramifications, your first...</p><span class="more">Read More</span></div>
      </div>
      <div class="item">
        <svg width="27" height="27" viewBox="0 0 27 27" fill="none" stroke="#777"><rect x="1" y="5" width="21" height="21"/><path d="M5 1h21v21M5 11h8M5 15h13M5 19h13M15 10h4v3h-4z"/></svg>
        <div><h4>How to Protect Yourself During Construction/Renovations</h4><p>Construction and renovation expenses can be substantial, often in excess of $100,000.00. While many projects go smoothly, others do not. Contractors (or subcontractors) can fail to build to spe...</p><span class="more">Read More</span></div>
      </div>
    </div>
  </div>
</section>

<section class="wins">
  <div class="wrap">
    <div class="block-head"><h2>Case Wins</h2><span class="viewall">View All</span></div>
    <div class="cols">
      <div class="item">
        <svg width="27" height="27" viewBox="0 0 27 27" fill="none" stroke="#777"><path d="M3 2h21v23H3zM8 2v3h11V2M13 9v11M8 20h11M7 12h12M7 12l-2 5h4zM19 12l-2 5h4z"/></svg>
        <div><h4>Injunction –</h4><p>Secured a Court Order appointing a Receiver and directing the Sheriff to seize all assets of a transportation company, resulting in approximately 20 buses and shuttles being pulled off the road and impounded.</p></div>
      </div>
      <div class="item">
        <svg width="27" height="27" viewBox="0 0 27 27" fill="none" stroke="#777"><path d="M3 2h21v23H3zM8 2v3h11V2M13 9v11M8 20h11M7 12h12M7 12l-2 5h4zM19 12l-2 5h4z"/></svg>
        <div><h4>Summary – Judgment</h4><p>Defeated Defendant's motion for summary judgment on a <strong>multi-million dollar</strong> claim involving a minor who suffered severe brain injuries.</p></div>
      </div>
      <div class="item">
        <svg width="27" height="27" viewBox="0 0 27 27" fill="none" stroke="#777"><path d="M3 2h21v23H3zM8 2v3h11V2M13 9v11M8 20h11M7 12h12M7 12l-2 5h4zM19 12l-2 5h4z"/></svg>
        <div><h4>$295,000.00 –</h4><p>Settlement for soft tissue and psychological injuries in a claim involving <b>professional negligence</b>.</p></div>
      </div>
    </div>
  </div>
</section>

<section class="stats">
  <div class="stats-bg" role="img" aria-label="Soft grey checkered tech pattern background"></div>
  <div class="stats-person" role="img" aria-label="Portrait of lead lawyer in suit and red tie"></div>
  <svg class="links" width="1200" height="397" viewBox="0 0 1200 397">
    <g stroke="#0f3a5a" stroke-width="1.5" fill="none">
      <path d="M353 109 495 252M386 293H447M845 109 705 252M812 293H759"/>
    </g>
    <g fill="#0f3a5a"><circle cx="353" cy="109" r="4"/><circle cx="386" cy="293" r="4"/><circle cx="845" cy="109" r="4"/><circle cx="812" cy="293" r="4"/></g>
    <g fill="rgba(90,140,190,.35)" stroke="#0f3a5a" stroke-width="1.5"><circle cx="495" cy="252" r="15"/><circle cx="447" cy="293" r="15"/><circle cx="705" cy="252" r="15"/><circle cx="759" cy="293" r="15"/></g>
  </svg>
  <div class="stat" style="left:152px;top:59px"><b>17+</b><span>Years of Litigation</span></div>
  <div class="stat" style="left:187px;top:242px"><b>15</b><span>Awards</span></div>
  <div class="stat" style="left:845px;top:59px"><b>234</b><span>Cases Won</span></div>
  <div class="stat" style="left:812px;top:242px"><b>5.0</b><span>Customers Rating</span></div>
</section>

<section class="reviews">
  <div class="wrap">
    <h2 class="titled">What Our Clients Are Saying</h2>
    <div class="review">
      <div class="who">
        <div class="avatar" role="img" aria-label="Client photo"></div>
        <div><h4>Renee Holloway</h4><small>Litigation Client</small></div>
        <div class="stars">
          <svg width="23" height="22" viewBox="0 0 24 23"><path d="M12 1l3.2 7 7.6.8-5.7 5.1 1.6 7.5L12 17.6l-6.7 3.8 1.6-7.5L1.2 8.8 8.8 8z" fill="#f5b301"/></svg>
          <svg width="23" height="22" viewBox="0 0 24 23"><path d="M12 1l3.2 7 7.6.8-5.7 5.1 1.6 7.5L12 17.6l-6.7 3.8 1.6-7.5L1.2 8.8 8.8 8z" fill="#f5b301"/></svg>
          <svg width="23" height="22" viewBox="0 0 24 23"><path d="M12 1l3.2 7 7.6.8-5.7 5.1 1.6 7.5L12 17.6l-6.7 3.8 1.6-7.5L1.2 8.8 8.8 8z" fill="#f5b301"/></svg>
          <svg width="23" height="22" viewBox="0 0 24 23"><path d="M12 1l3.2 7 7.6.8-5.7 5.1 1.6 7.5L12 17.6l-6.7 3.8 1.6-7.5L1.2 8.8 8.8 8z" fill="#f5b301"/></svg>
          <svg width="23" height="22" viewBox="0 0 24 23"><path d="M12 1l3.2 7 7.6.8-5.7 5.1 1.6 7.5L12 17.6l-6.7 3.8 1.6-7.5L1.2 8.8 8.8 8z" fill="#f5b301"/></svg>
        </div>
      </div>
      <p>I cannot say enough about having Daniel Dorvant as my lawyer! I found him during a very difficult and stressful time and was so nervous about finding a good lawyer after having a few bad experiences. The experience that I had with Daniel eased ALL of that anxiety for me! He worked very very hard on my settlement and was very reassuring and truly cared about my situation. I always knew what was going on with my case as he always kept me updated with phone calls, emails and everything that was pertained to my case… I highly recommend Daniel Dorvant as a lawyer and if you would like someone who is thorough and who truly cares about your case and you as a person then this is the man to go to!!!</p>
      <div class="dots"><i></i><i></i><i></i><i></i><i></i></div>
    </div>
  </div>
</section>

<footer class="footer">
  <div class="wrap">
    <div class="fleft">
      <div class="brand"><span class="brand-mark"></span><div class="brand-name">Dorvant<br>Legal</div></div>
      <ul class="flist">
        <li><span class="ico"><svg width="11" height="11" viewBox="0 0 12 12"><path d="M6 1a3.5 3.5 0 0 0-3.5 3.5C2.5 7.5 6 11 6 11s3.5-3.5 3.5-6.5A3.5 3.5 0 0 0 6 1z" fill="none" stroke="#fff"/></svg></span>GTA - Hamilton - Niagara</li>
        <li><span class="ico"><svg width="11" height="11" viewBox="0 0 12 12"><path d="M2 1.5h2.5l1 2.5-1.5 1a7 7 0 0 0 3 3l1-1.5 2.5 1V10a1 1 0 0 1-1 1A9 9 0 0 1 1 2.5a1 1 0 0 1 1-1z" fill="none" stroke="#fff"/></svg></span><a>555.214.7730</a></li>
        <li><span class="ico"><svg width="11" height="9" viewBox="0 0 12 10"><rect x=".5" y=".5" width="11" height="9" fill="none" stroke="#fff"/><path d="M.5 .5 6 5l5.5-4.5" fill="none" stroke="#fff"/></svg></span><a>info@dorvantlegal.ca</a></li>
      </ul>
    </div>
    <div class="fright">
      <p>Dorvant Legal is a boutique law office concentrating in Complex Business Litigation, Professional Negligence, and Insurance Coverage Disputes. Our innovative and pugnacious approach gets results for our clients in the Greater Toronto Area. HST #000000000RT0001</p>
      <div class="offices">
        <div><h5>Hamilton Office</h5>48 Carrow Street E,<br>Ground Floor Hamilton,<br>ON L8A 0B2</div>
        <div><h5>Toronto Office</h5>210 Front Street W #3100,<br>Toronto,<br>ON M5A 0C4</div>
        <div><h5>Niagara Office</h5>9 Alder Lane,<br>Virgil,<br>ON L0S 0A3</div>
      </div>
    </div>
  </div>
</footer>
<div class="bottom">
  <div class="wrap">
    <div>© 2023 Dorvant Legal. All Rights Reserved. <a>Sitemap</a></div>
    <div class="share">Share this page: <i></i><i></i><i></i><i></i><i></i><i></i></div>
  </div>
</div>

</body>
</html>
```